Branvique needs a business Card Design

We are looking for a business card Design for our new Managed Service Provider Company, Branvique. Branvique encompasses everything IT for the average medium sized business. Our primary services are help desk support, cyber-security (malware and ransomware protection), and Disaster Recovery systems. We would like the design to have a very clean and professional look, with a very minimalist feel.

Target Market(s)

Medium to large sized businesses

Industry/Entity Type

It Service

Contact Information for Business Card

Name GoesHere
name@branvique.com
O: 555-382-6047
C: 555-731-5820

Font styles to use
Other font styles liked:
• Poppins Font Only Please

Colors

Designer to choose only greyscale colors for use in the design.

Requirements
Must have
• Logo included
Nice to have
• Cutting Edge, innovative, minimalistic, elegant

```html
<!DOCTYPE html>
<html lang="en">
<head>
<meta charset="utf-8">
<title>Branvique Business Card</title>
<link rel="stylesheet" href="https://fonts.googleapis.com/css2?family=Poppins:wght@300;400&display=swap">
<style>
  :root {
    --ink: #222222;
    --paper: #ffffff;
    --mark: #d6d6d6;
    --backdrop: #e3e3e3;
  }
  html, body {
    margin: 0;
    padding: 0;
    width: 1200px;
    height: 686px;
    overflow: hidden;
    background: var(--backdrop);
  }
  .canvas {
    width: 1200px;
    height: 686px;
    display: flex;
    align-items: center;
    justify-content: center;
  }
  .business-card {
    display: block;
    width: 1040px;
    height: 594px;
    font-family: "Poppins", sans-serif;
  }
  .card-face { fill: var(--paper); }
  .brand-panel { fill: var(--ink); }
  .brand-symbol { fill: var(--mark); }
  .divider { stroke: var(--ink); stroke-width: 2; }
  .wordmark {
    fill: var(--paper);
    font-weight: 400;
    font-size: 40px;
  }
  .person-name { fill: var(--ink); font-size: 28px; font-weight: 400; }
  .person-role { fill: var(--ink); font-size: 21px; font-weight: 300; }
  .contact-line { fill: var(--ink); font-size: 17px; font-weight: 300; }
</style>
</head>
<body>
<main class="canvas">
  <svg class="business-card" viewBox="0 0 756 432" xmlns="http://www.w3.org/2000/svg" aria-label="Branvique business card">
    <rect class="card-face" x="0" y="0" width="756" height="432"/>
    <polygon class="brand-panel" points="0,0 756,0 0,432"/>

    <circle class="brand-symbol" cx="180" cy="106" r="42"/>

    <g transform="rotate(-29.75 252 238)">
      <text class="wordmark" x="252" y="252" text-anchor="middle" textLength="430" lengthAdjust="spacing">BRANVIQUE</text>
    </g>

    <line class="divider" x1="407" y1="244" x2="407" y2="396"/>

    <text class="person-name" x="441" y="266">Alex Morgan</text>
    <text class="person-role" x="441" y="295">Sales Manager</text>

    <text class="contact-line" x="441" y="349">E :  alex_morgan@branvique.com</text>
    <text class="contact-line" x="441" y="370">O:  555-382-6047</text>
    <text class="contact-line" x="441" y="391">C:  555-731-5820</text>
  </svg>
</main>
</body>
</html>
```